Mortgage Lender needs Flyers Designed

We are a wholesale mortgage lender providing mortgage services throughout the United States to mortgage brokers. We just merged with a company and need to redesign their product flyers and matrices so they are more in line with a modern and sleek look. We provide residential and commercial mortgage financing options. I have attached a document labeled FULL STACK. This is the current flyer set that needs to be redesigned for my company. There are 10 programs featured in the document. The first two pages provide a product overview and the following 17 pages are the matrices for each product. I need a design set created in either Adobe Photoshop or Adobe Indesign so we can edit the content as necessary.

Target Market(s)

Mortgage Brokers in the United States

Industry/Entity Type

Finance, Mortgage

Font styles to use
Serif
Sans Serif

Requirements
Must have
• Must include all ten programs and must be designed using Adobe Photoshop or Adobe InDesign (preferred)
Nice to have
• Great graphics and clean modern feel.
Should not have
• Typos, hard to edit fields, should not look very similar to the FULL STACK pdf attached.

```html
<!DOCTYPE html>
<html lang="en">
<head>
<meta charset="utf-8">
<title>Equity Horizon HELOC Program Matrix</title>
<link href="https://fonts.googleapis.com/css2?family=Poppins:ital,wght@0,400;0,500;0,600;0,700;1,500&family=Montserrat:wght@500;700;800&display=swap" rel="stylesheet">
<style>
:root{
  --backdrop:#a0ad97;
  --paper:#ffffff;
  --forest:#3f6833;
  --leaf:#4f8a2c;
  --lime:#d8e23f;
  --ink:#1d1d1d;
  --cell:#ececec;
  --fico:#e6e8c0;
  --black:#0b0b0b;
}
*{box-sizing:border-box;margin:0;padding:0}
html,body{width:1009px;height:1200px;overflow:hidden;background:var(--backdrop)}
body{font-family:"Poppins",sans-serif;color:var(--ink)}
.sheet{position:absolute;left:40px;top:0;width:1298px;height:1679px;background:var(--paper);transform:scale(0.7147);transform-origin:0 0;overflow:hidden}
.abs{position:absolute}
.header-art{position:absolute;left:0;top:0;width:1298px;height:225px}
.title{position:absolute;right:71px;top:62px;text-align:right;color:#fff;font-family:"Montserrat",sans-serif}
.title-main{font-size:51px;line-height:56px;font-weight:500;letter-spacing:.5px}
.title-main b{font-weight:800}
.title-sub{font-size:34px;line-height:40px;color:var(--lime);font-weight:500;letter-spacing:2px}
.title-sub b{font-weight:700}
.brand{position:absolute;left:66px;top:108px;display:flex;align-items:center;gap:18px}
.brand-mark{width:46px;height:46px;border-radius:50%;background:var(--forest)}
.brand-text{font-size:34px;font-weight:600;color:var(--forest);line-height:38px}
.brand-url{font-size:34px;font-weight:600;color:var(--forest)}
.brand-web{position:absolute;left:130px;top:160px;font-size:14px;font-weight:600;color:var(--forest);letter-spacing:5px}
.intro{left:63px;top:287px;width:525px;font-size:15px;line-height:18px}
.sec-title{font-size:19px;font-weight:700;letter-spacing:1.3px;line-height:22px}
.sec-sub{font-size:14px;font-weight:600;color:var(--leaf);line-height:18px}
.matrix{display:grid;grid-template-columns:169px 109px 110px 110px;column-gap:6px;row-gap:4px;width:517px}
.matrix .h{height:45px;border-radius:4px;background:var(--forest);color:var(--lime);font-size:14px;line-height:16px;display:flex;align-items:center;justify-content:center;text-align:center}
.matrix .h.fico{background:var(--black);color:var(--lime)}
.matrix .c{height:27px;border-radius:3px;background:var(--cell);font-size:13.5px;display:flex;align-items:center;justify-content:center}
.matrix .h + .h{}
.matrix .gap{grid-column:1/-1;height:0}
.full .c.f{background:var(--fico)}
.note{left:63px;top:914px;width:525px;font-size:13.5px;line-height:18px}
.photo{left:63px;top:982px;width:517px;height:258px;border:3px solid var(--forest);background:linear-gradient(120deg,#f3e6d6 0%,#e7d8cb 30%,#c9bdb7 55%,#ddd9d8 80%,#cfcfd4 100%)}
.loan{left:63px;top:1279px;width:518px;display:grid;grid-template-columns:130px 384px;gap:6px 4px}
.loan .h{height:45px;border-radius:4px;display:flex;align-items:center;padding-left:14px;font-size:12.5px;font-weight:600;color:var(--lime);background:var(--forest)}
.loan .h.first{background:var(--black)}
.loan .k{background:var(--cell);border-radius:4px;display:flex;align-items:center;padding-left:32px;font-size:16px}
.loan .v{background:var(--cell);border-radius:4px;padding:8px 20px 14px 26px;font-size:14.5px;line-height:21px}
.loan ol{padding-left:18px}
.loan ul{list-style:none;padding-left:0}
.loan ul li{display:flex;align-items:center;gap:8px;font-size:14px}
.dot{width:8px;height:8px;border-radius:50%;background:var(--leaf);flex:none}
.req{left:638px;top:283px;width:620px}
.req h2{font-size:19px;font-weight:700;letter-spacing:1.3px;margin-left:3px}
.req-row{position:absolute;left:0;width:620px;display:grid;grid-template-columns:127px 1fr;font-size:14.5px;line-height:18px}
.req-row .lbl{color:var(--leaf);font-weight:600}
.req-row p + p{margin-top:7px}
.req-row strong{font-weight:600}
.recert{left:635px;top:1022px;width:610px;font-size:17px;line-height:20px}
.recert h3{font-size:20px;line-height:23px;font-weight:700;color:var(--leaf)}
.recert .p{margin-top:0}
.recert ul{list-style:none}
.recert li{display:flex;gap:10px;margin-bottom:13px}
.recert li .dot{margin-top:6px}
.recert em{font-weight:500;color:var(--ink)}
</style>
</head>
<body>
<main class="sheet">
  <svg class="header-art" viewBox="0 0 1298 225" aria-hidden="true">
    <rect x="0" y="9" width="528" height="8" fill="#0b0b0b"/>
    <polygon points="525,0 1298,0 1298,211 620,211" fill="#3f6833"/>
    <polygon points="737,211 1298,211 1298,221 743,221" fill="#0b0b0b"/>
  </svg>

  <div class="brand"><span class="brand-mark"></span><span class="brand-text">Crestline Lending Group</span></div>
  <div class="brand-web">CRESTLINELEND.COM</div>

  <div class="title">
    <div class="title-main"><b>EQUITY</b> HORIZON</div>
    <div class="title-sub"><b>HELOC</b> PROGRAM MATRIX</div>
  </div>

  <p class="abs intro">The below credit matrix is designed to be used in conjunction with the Birchway Funding Equity Horizon Guidelines (hereinafter referred to as guides). Any topics not specifically addressed within the Birchway Funding Equity Horizon HELOC Program Overlay below should be reviewed within the guides.</p>

  <section class="abs" style="left:63px;top:414px">
    <h2 class="sec-title">FULL DOCUMENTATION</h2>
    <div class="sec-sub">Maximum HCLTV</div>
    <div class="matrix full" style="margin-top:5px">
      <div class="h fico">FICO</div><div class="h">Owner<br>Occupied</div><div class="h">2nd Home</div><div class="h">Investment</div>
      <div class="c f">740</div><div class="c">90</div><div class="c">90</div><div class="c">85</div>
      <div class="c f">700 - 739</div><div class="c">90</div><div class="c">90</div><div class="c">85</div>
      <div class="c f">680 - 699</div><div class="c">90</div><div class="c">90</div><div class="c">85</div>
      <div class="c f">660 - 679</div><div class="c">70</div><div class="c">60</div><div class="c">60</div>
    </div>
  </section>

  <section class="abs" style="left:63px;top:684px">
    <h2 class="sec-title">BANK STATEMENTS</h2>
    <div class="sec-sub">Maximum HCLTV</div>
    <div class="matrix" style="margin-top:5px">
      <div class="h fico">FICO</div><div class="h">Owner<br>Occupied</div><div class="h">2nd Home</div><div class="h">Investment</div>
      <div class="c">740</div><div class="c">85</div><div class="c">85</div><div class="c">80</div>
      <div class="c">700 - 739</div><div class="c">85</div><div class="c">85</div><div class="c">80</div>
      <div class="c">680 - 699</div><div class="c">85</div><div class="c">85</div><div class="c">80</div>
      <div class="c">660 - 679</div><div class="c">70</div><div class="c">60</div><div class="c">60</div>
    </div>
  </section>

  <p class="abs note">Full appraisals required on all 1st lien positions.&nbsp; Interior BPO required for loans with CLTV &gt; 80%.</p>

  <div class="abs photo" role="img" aria-label="Photo of hands typing on a laptop beside rising stacks of coins in warm light"></div>

  <div class="abs loan">
    <div class="h first">Loan Amount</div><div class="h">Details</div>
    <div class="k">≤$250k</div>
    <div class="v">
      <ol>
        <li>AVM with exterior property inspection with the following requirement:
          <ul>
            <li><span class="dot"></span>Max 90 CLTV</li>
            <li><span class="dot"></span>Minimum confidence score of 90%</li>
          </ul>
        </li>
        <li>Drive by appraisal</li>
        <li>Full appraisal</li>
        <li>Use prior appraisal (see requirements)</li>
      </ol>
    </div>
    <div class="k">&gt;250k</div>
    <div class="v" style="padding-top:14px">
      <ol>
        <li>Full interior appraisal (1004/1025/1073)</li>
        <li>Use prior appraisal (see requirements)</li>
      </ol>
    </div>
  </div>

  <section class="abs req" style="height:700px">
    <h2>GENERAL REQUIREMENTS</h2>
    <div class="req-row" style="top:35px"><div class="lbl">Product Type</div><div>Variable rate (Index plus a margin), 3 or 5 year IO draw period with a fully amortizing repayment period.&nbsp; 30, 25, 20, and 15 year amortization terms allowed</div></div>
    <div class="req-row" style="top:122px"><div class="lbl">HELOC<br>Requirements</div><div>
      <p><strong>Index:</strong> Prime rate as published in the Ledger Daily on the 1st of the month - highest range used if range is published</p>
      <p><strong>Initial Draw:</strong> Minimum of 50% of the total line amount and no less than $150k</p>
      <p><strong>Additional Draw:</strong> Prohibited during the first 90 days following closing date.&nbsp; Minimum $1k not to exceed credit limit</p>
      <p><strong>Loan Payback:</strong> No principal payments allowed during first 90 days. Any principal payback may be considered an EPO</p>
    </div></div>
    <div class="req-row" style="top:323px"><div class="lbl">Line/Loan<br>Amount</div><div>$150k - $500k<br>Maximum total financing is limited to $5MM<br>(total amount of 1st and 2nd lien combined)</div></div>
    <div class="req-row" style="top:407px"><div class="lbl">Line Positions</div><div>1st and 2nd lien positions only</div></div>
    <div class="req-row" style="top:450px"><div class="lbl">Occupancy</div><div>Owner-occupied, second homes, investment<br>(limited to 10 financed properties)</div></div>
    <div class="req-row" style="top:516px"><div class="lbl">Debt to<br>Income</div><div>
      <p>Max 50% DTI with 700+ FICO and $3,500 residual monthly income</p>
      <p>Max 45% DTI in all other scenarios</p>
      <p>30-yr fully amortized payment based on start rate +2% and the total credit limit used to qualify if floating rate</p>
    </div></div>
    <div class="req-row" style="top:630px"><div class="lbl">Early<br>Termination</div><div>5% penalty if terminated within the first 12 months unless otherwise prohibited by Federal or State law</div></div>
  </section>

  <section class="abs recert">
    <h3>Recertification of an existing appraisal is acceptable when the following requirements are met:</h3>
    <p style="margin-top:26px">Report has been completed within 12 months of application date</p>
    <p style="margin-top:20px">Current appraisal provided must be on form 1004 (single family), 1025 (multi-family), or 1073 (condo)</p>
    <p style="margin-top:20px;font-weight:600">One of the following are required:</p>
    <ul>
      <li><span class="dot"></span><span>AVM supporting value within 10% variance and Property Condition Inspection (PCI) is required when effective age of the appraisal is greater than 90 days</span></li>
      <li><span class="dot"></span><span>A Collateral Desktop Analysis (CDA) and Property Condition Inspection (PCI) are required and will be ordered by the lender to validate any use of an existing appraisal</span></li>
      <li><span class="dot"></span><span>CDA risk score must be low or moderate with no additional review recommended by reviewer - up to 10% variance in value</span></li>
      <li><span class="dot"></span><span>CDA analysis commentary contains no comments that adversely impact value, marketability, or condition of the property</span></li>
      <li><span class="dot"></span><span>CDA home data index must support either a neutral or increasing market trend.</span></li>
    </ul>
    <p style="margin-top:6px"><em>CLTV will be calculated as the lower of the purchase price/CDA value or the appraised value</em></p>
  </section>
</main>
</body>
</html>
```